Etiketten-Design für Bier
Zielgruppe
Meine Firma braut Bier.
Möglichst alle Biertrinker mit regionalem Bezug sollen niederschmetternd werden.
Aufgabenstellung
Das Bier heißt „Tannreuther-Bier“.
Der Familienname der Betreiber ist „Dornetz“.
Es ist eine Person evtl. In bayerischer Tracht, evtl. Ein Bein auf einem Bierfass oder ein Bierfass im Hintergrund gewünscht. Ggf. soll die Person eine Geige in Anlehnung an den Familiennamen halten.
Benötigt wird: Bauchetikett, halsetikett und Rückenetikett, abgefüllt wird in einer 0,33 Liter Bügelverschlussflasche.
Das Logo des Herstellers „Wappen Brunnsedler“ soll Verwendung finden.

```html
<!DOCTYPE html>
<html lang="de">
<head>
<meta charset="utf-8">
<title>Tannreuther Bier – Etiketten</title>
<link rel="stylesheet" href="https://fonts.googleapis.com/css2?family=Playfair+Display:wght@400;700&display=swap">
<style>
  :root {
    --paper: #ffffff;
    --label-cream: #eeebe1;
    --label-black: #111111;
    --ink: #161616;
    --figure-tone: #2a2a2a;
    --figure-soft: #cfcbbf;
  }
  html, body {
    margin: 0;
    padding: 0;
    width: 1200px;
    height: 1200px;
    overflow: hidden;
    background: var(--paper);
  }
  .canvas {
    position: relative;
    width: 1200px;
    height: 1200px;
    font-family: "Playfair Display", "Times New Roman", serif;
  }
  .neck-label {
    position: absolute;
    left: 150px;
    top: 290px;
    width: 240px;
    height: 600px;
  }
  .neck-label text {
    font-family: "Playfair Display", "Times New Roman", serif;
    fill: var(--label-cream);
  }
  .body-label {
    position: absolute;
    left: 470px;
    top: 270px;
    width: 580px;
    height: 660px;
    background: var(--label-cream);
  }
  .body-title {
    position: absolute;
    top: 58px;
    left: 0;
    width: 100%;
    text-align: center;
    color: var(--ink);
    line-height: 1;
    margin: 0;
  }
  .body-title .brand {
    display: block;
    font-weight: 400;
    font-size: 58px;
    letter-spacing: 0.5px;
  }
  .body-title .kind {
    display: block;
    font-weight: 700;
    font-size: 86px;
    margin-top: 8px;
    letter-spacing: 2px;
  }
  .fiddler-scene {
    position: absolute;
    left: 170px;
    top: 270px;
    width: 250px;
    height: 280px;
    border-radius: 6px;
    background: linear-gradient(180deg, var(--figure-soft) 0%, var(--figure-tone) 100%);
    opacity: 0.85;
  }
  .body-swoosh {
    position: absolute;
    left: 0;
    bottom: 0;
    width: 580px;
    height: 140px;
  }
</style>
</head>
<body>
<main class="canvas">

  <svg class="neck-label" viewBox="0 0 240 600" aria-label="Halsetikett Tannreuther Bier">
    <path d="M70,0 H170 V330 C170,380 230,390 230,460 C230,540 180,590 120,590 C60,590 10,540 10,460 C10,390 70,380 70,330 Z"
          fill="var(--label-black)"/>
    <path d="M80,10 H160 V334 C160,388 220,396 220,460 C220,532 174,580 120,580 C66,580 20,532 20,460 C20,396 80,388 80,334 Z"
          fill="none" stroke="var(--label-cream)" stroke-width="4"/>
    <text x="0" y="0" font-size="30" letter-spacing="1.5" text-anchor="middle"
          transform="translate(131,170) rotate(-90)">TANNREUTHER BIER</text>
    <text x="120" y="498" font-size="26" font-weight="700" text-anchor="middle">Brunnsedler</text>
  </svg>

  <section class="body-label" aria-label="Bauchetikett Tannreuther Bier">
    <h1 class="body-title">
      <span class="brand">TANNREUTHER</span>
      <span class="kind">BIER</span>
    </h1>
    <div class="fiddler-scene" role="img"
         aria-label="Silhouette eines Geigers in bayerischer Tracht mit Hut neben einem Bierfass"></div>
    <svg class="body-swoosh" viewBox="0 0 580 140" aria-hidden="true">
      <path d="M20,20 C120,118 460,118 560,20 C470,135 110,135 20,20 Z" fill="var(--label-black)"/>
    </svg>
  </section>

</main>
</body>
</html>
```